We need a logo and landing page designed. We are a full-service general contractor based in Tempe Arizona. We can provide all phases of construction from design to completion. We specialize in commercial and residential remodels, as well as ground-up construction. We will like to see designs that primarily used reds, blues, blacks, whites, etc. The design should be a professional yet fun, easy-to-read format. Our name is Oak Harbor Construction...I would like to see some designs that incorporate a "oak harbor" and some without.
The final design should communicate a professional, quality-driven, safety oriented full service business.

Target Market(s)

Building owners, land developers, homeowners

Industry/Entity Type

Commercial Construction

Coding

Coded - Design and coding required

Number of Pages Required

1 page

Font styles to use
Serif

Colors
0054AA
0677BA
7BADD7
CADEEF
E8F1F8
59FF00
82FF00
B8FF75
E3FFCB
F4FFEA
EE7325
F08F49
F5BC92
FAE3D3
FDF4ED
EB3D1F
EC4F4E
F09395
F8D3D4
FCEDEE

```html
<!DOCTYPE html>
<html lang="en">
<head>
<meta charset="utf-8">
<title>Oak Harbor Construction</title>
<link href="https://fonts.googleapis.com/css2?family=Poppins:wght@400;500;600;700&display=swap" rel="stylesheet">
<style>
:root{
  --blue:#0677BA;
  --blue-deep:#0054AA;
  --ink:#111111;
  --text:#444444;
  --white:#ffffff;
  --mist:#f1f1f1;
  --footer:#1e1e1e;
  --hero-a:#3a4a5c;
  --hero-b:#1d2836;
}
*{margin:0;padding:0;box-sizing:border-box}
html,body{width:1200px;height:1000px;overflow:hidden;background:#fff;font-family:"Poppins",sans-serif;color:var(--ink)}
.page{position:absolute;left:428px;top:0;width:344px;height:1000px;background:var(--white);overflow:hidden}
.abs{position:absolute}
/* hero */
.hero{left:0;top:0;width:344px;height:176px;background:linear-gradient(160deg,#6b7a88 0%,var(--hero-a) 40%,var(--hero-b) 100%)}
.hero-shade{left:0;top:0;width:344px;height:176px;background:rgba(10,20,35,.3)}
.brand{left:26px;top:10px;font-size:5.5px;font-weight:700;color:var(--white)}
.nav{left:102px;top:11px;display:flex;gap:8px;font-size:3.6px;color:var(--white)}
.btn{background:var(--blue);color:var(--white);font-size:3.4px;font-weight:600;display:flex;align-items:center;justify-content:center;white-space:nowrap}
.nav-btn{left:261px;top:7px;width:57px;height:13px}
.hero-title{left:0;width:344px;top:52px;text-align:center;font-size:10.5px;line-height:12.5px;font-weight:700;color:var(--white)}
.hero-copy{left:100px;width:144px;top:82px;text-align:center;font-size:3.5px;line-height:7px;color:#e6e6e6}
.hero-btn{left:155px;top:111px;width:34px;height:10px}
.dots{top:169px;left:0;width:344px;display:flex;justify-content:center;gap:2px}
.dots i{width:3px;height:3px;border-radius:50%;background:#fff;display:block}
.dots i.on{background:var(--blue)}
/* about */
.h2{left:0;width:344px;text-align:center;font-weight:700;color:var(--ink)}
.h2 b{color:var(--blue);font-weight:700}
.about-title{top:192px;font-size:10px;color:var(--blue)}
.about-copy{left:100px;width:144px;top:209px;text-align:center;font-size:3.5px;line-height:7px;color:var(--text)}
.video{left:65px;top:241px;width:214px;height:88px;background:linear-gradient(120deg,#55616d,#3a424b 50%,#7a6a4d);border:1px solid #222}
.play{left:158px;top:273px;width:24px;height:24px;border-radius:50%;background:var(--white);display:flex;align-items:center;justify-content:center}
.work-title{top:345px;font-size:10.5px;line-height:13px}
.service{width:140px;height:26px;display:flex;gap:4px}
.service .ico{width:18px;height:26px;background:var(--blue);flex:none;display:flex;align-items:center;justify-content:center}
.service h3{font-size:5px;font-weight:600;line-height:6px;margin-bottom:1px}
.service p{font-size:3.2px;line-height:5.6px;color:var(--text);height:17px;overflow:hidden}
/* projects */
.projects{left:0;top:503px;width:344px;height:149px;background:var(--mist)}
.proj-title{top:513px;font-size:10px}
.shot{width:94px;height:48px}
/* testimonials */
.testi-left{left:0;top:670px;width:172px;height:87px;background:var(--mist)}
.testi-right{left:172px;top:670px;width:172px;height:87px;background:var(--blue)}
.testi-title{left:0;top:702px;width:172px;text-align:center;font-size:10px;font-weight:700}
.testi-title b{color:var(--blue)}
.testi-sub{left:0;width:172px;top:716px;text-align:center;font-size:3.6px}
.avatar{left:162px;top:702px;width:22px;height:22px;border-radius:50%;background:linear-gradient(#6c757d,#2f3942);border:1.5px solid #fff}
.quote{left:196px;width:108px;top:693px;text-align:center;font-size:3.5px;line-height:6px;color:#eaf3fa}
.quote-name{left:196px;width:108px;top:716px;text-align:center;font-size:4px;font-weight:600;color:#fff}
.tdots{left:244px;top:727px;display:flex;gap:2px}
.tdots i{width:3px;height:3px;border-radius:50%;background:#fff;display:block}
/* contact */
.cta-title{left:35px;top:814px;font-size:7.5px;font-weight:500}
.cta-title b{color:var(--blue);font-weight:500}
.cta-copy{left:35px;top:827px;width:135px;font-size:3.4px;line-height:6.1px;color:var(--text)}
.cta-btn{left:35px;top:865px;width:35px;height:10px}
.form{left:185px;top:776px;width:124px;height:144px;background:var(--mist)}
.field{left:190px;width:114px;height:14px;background:#fff;font-size:3.4px;padding:4px 3px;color:#222}
.submit{left:190px;top:903px;width:114px;height:9px}
/* footer */
.footer{left:0;top:938px;width:344px;height:62px;background:var(--footer);color:#fff}
.f-brand{left:26px;top:947px;font-size:5.5px;font-weight:700;color:#fff}
.f-brand b{color:var(--blue)}
.f-call{left:26px;top:957px;font-size:5.5px;color:#fff;display:flex;align-items:center;gap:3px}
.f-call small{font-size:3.4px}
.f-small{font-size:3.2px;line-height:5.6px;color:#ddd}
.f-head{font-size:5px;font-weight:600;color:#fff}
.f-list{font-size:3.2px;line-height:5.6px;color:#ddd}
.f-list .on{color:var(--blue)}
.socials{left:258px;top:967px;display:flex;gap:2px}
.socials i{width:6px;height:6px;border-radius:50%;background:#fff;display:block}
</style>
</head>
<body>
<main class="page">
  <!-- hero -->
  <section class="abs hero" role="img" aria-label="Excavator at a construction site with city skyline at dusk"></section>
  <div class="abs hero-shade"></div>
  <div class="abs brand">Oak Harbor Construction</div>
  <nav class="abs nav"><span>Home</span><span>About</span><span>Service</span><span>Testimonials</span><span>Gallery</span><span>Contact Us</span></nav>
  <div class="abs btn nav-btn">Request Investment Package</div>
  <h1 class="abs hero-title">Construction Solution We<br>Build Your Dream.</h1>
  <p class="abs hero-copy">Lorem ipsum is simply dummy text of the printing and typesetting industry. Lorem Ipsum has been the industry's standard dummy text ever since the 1500s with modern layout tools and kits.</p>
  <div class="abs btn hero-btn">Contact Us</div>
  <div class="abs dots"><i></i><i class="on"></i><i></i></div>

  <!-- about -->
  <h2 class="abs h2 about-title">About Us</h2>
  <p class="abs about-copy">Lorem ipsum is simply dummy text of the printing and typesetting industry. Lorem Ipsum has been the industry's standard dummy text ever since the 1500s with modern layout tools and kits.</p>
  <div class="abs video" role="img" aria-label="Video still of workers in safety vests reviewing plans on site"></div>
  <div class="abs play"><svg width="8" height="8" viewBox="0 0 8 8"><path d="M2 1 L7 4 L2 7 Z" fill="#0677BA"/></svg></div>

  <h2 class="abs h2 work-title">We Work With <b>Contractors,</b><br><b>Developer</b> And <b>Property Manager</b></h2>

  <div class="abs service" style="left:27px;top:380px"><div class="ico"><svg width="10" height="10" viewBox="0 0 10 10" fill="none" stroke="#fff" stroke-width=".8"><rect x="1" y="1" width="8" height="8"/><path d="M1 4h8M4 4v5"/></svg></div><div><h3>Concrete Polishings</h3><p>Construction is a general term meaning the art and science to form objects, systems, or organizations, and comes from Latin construere "together" and struere "to pile up".</p></div></div>
  <div class="abs service" style="left:182px;top:380px"><div class="ico"><svg width="10" height="10" viewBox="0 0 10 10" fill="none" stroke="#fff" stroke-width=".8"><path d="M2 1h6v3H2zM5 4v5M3 9h4"/></svg></div><div><h3>Floor Coatings</h3><p>In its most widely used context, construction covers the processes involved in delivering buildings, infrastructure, industrial facilities and associated activities through to the end of their life.</p></div></div>
  <div class="abs service" style="left:27px;top:419px"><div class="ico"><svg width="10" height="10" viewBox="0 0 10 10" fill="none" stroke="#fff" stroke-width=".8"><path d="M1 8l6-6M5 2h2v2M1 9h8"/></svg></div><div><h3>Concrete Repairs</h3><p>The construction industry contributes significantly to many countries' gross domestic products. Global expenditure on construction activities was about four trillion dollars in 2012.</p></div></div>
  <div class="abs service" style="left:182px;top:419px"><div class="ico"><svg width="10" height="10" viewBox="0 0 10 10" fill="none" stroke="#fff" stroke-width=".8"><path d="M2 2l6 6M8 2L2 8"/><circle cx="5" cy="5" r="1.2"/></svg></div><div><h3>Surface Preparation</h3><p>Although the construction industry promotes economic development and brings many non-monetary benefits to many countries, it is one of the most hazardous industries.</p></div></div>
  <div class="abs service" style="left:27px;top:458px"><div class="ico"><svg width="10" height="10" viewBox="0 0 10 10" fill="none" stroke="#fff" stroke-width=".8"><path d="M5 1C3 4 2 5.5 2 6.5a3 3 0 006 0C8 5.5 7 4 5 1z"/></svg></div><div><h3>Water Proffings</h3><p>Construction is a general term meaning the art and science to form objects, systems, or organizations, and comes from Latin construere "together" and struere "to pile up".</p></div></div>
  <div class="abs service" style="left:182px;top:458px"><div class="ico"><svg width="10" height="10" viewBox="0 0 10 10" fill="none" stroke="#fff" stroke-width=".8"><path d="M2 6a3 3 0 016 0zM1 6h8M5 3V2"/></svg></div><div><h3>Concrete and stealing cleanings</h3><p>In its most widely used context, construction covers the processes involved in delivering buildings, infrastructure, industrial facilities and associated activities through to the end of their life.</p></div></div>

  <!-- projects -->
  <section class="abs projects"></section>
  <h2 class="abs h2 proj-title">Our <b>Project</b></h2>
  <div class="abs shot" style="left:27px;top:539px;background:linear-gradient(160deg,#8fb6d8,#8a5a48)" role="img" aria-label="Building frame under construction"></div>
  <div class="abs shot" style="left:125px;top:539px;background:linear-gradient(180deg,#c9dbe8,#7d7f76)" role="img" aria-label="Construction site with cranes and towers"></div>
  <div class="abs shot" style="left:223px;top:539px;background:linear-gradient(180deg,#e9a57e,#5b5a5f)" role="img" aria-label="Modern apartment buildings at sunset"></div>
  <div class="abs shot" style="left:27px;top:590px;background:linear-gradient(180deg,#5e93c9,#8c6a4e)" role="img" aria-label="Tower with scaffolding against blue sky"></div>
  <div class="abs shot" style="left:125px;top:590px;background:linear-gradient(160deg,#4d86c6,#3e4b44 60%,#4f7a3a)" role="img" aria-label="High-rise under construction behind trees"></div>
  <div class="abs shot" style="left:223px;top:590px;background:linear-gradient(180deg,#b9ccdc,#6f7f90)" role="img" aria-label="City skyline of glass towers"></div>

  <!-- testimonials -->
  <section class="abs testi-left"></section>
  <section class="abs testi-right"></section>
  <h2 class="abs testi-title">Our <b>Testimonials</b></h2>
  <p class="abs testi-sub">Includes Business For Professionals</p>
  <div class="abs avatar" role="img" aria-label="Client portrait"></div>
  <p class="abs quote">The first huts and shelters were constructed by hand or with simple tools. As cities grew during the bronze age, a class of professional craftsmen [6]</p>
  <p class="abs quote-name">Mark T. Ellison</p>
  <div class="abs tdots"><i></i><i></i><i></i></div>

  <!-- contact -->
  <h2 class="abs cta-title">Need Concrete Restoration <b>Fast?</b></h2>
  <p class="abs cta-copy">Lorem ipsum dolor sit amet, consectetur adipiscing elit, sed do eiusmod tempor incididunt ut labore et dolore magna aliqua. Quis ipsum suspendisse ultrices gravida. Risus commodo viverra maecenas accumsan lacus vel facilisis.</p>
  <div class="abs btn cta-btn">Contact Us</div>
  <section class="abs form"></section>
  <div class="abs field" style="top:783px">First Name</div>
  <div class="abs field" style="top:801px">Last Name</div>
  <div class="abs field" style="top:819px">Email</div>
  <div class="abs field" style="top:837px">Password</div>
  <div class="abs field" style="top:855px;height:44px">Message</div>
  <div class="abs btn submit">Submit</div>

  <!-- footer -->
  <footer class="abs footer"></footer>
  <div class="abs f-brand">Oak Harbor <b>Construction</b></div>
  <div class="abs f-call">Call Us <svg width="6" height="6" viewBox="0 0 6 6"><circle cx="3" cy="3" r="3" fill="#fff"/><path d="M2 1.6l.6.7-.3.5c.2.4.5.7.9.9l.5-.3.7.6-.4.6c-1.2-.2-2.3-1.3-2.5-2.5z" fill="#1e1e1e"/></svg><small>(+1) 480-555-0142</small></div>
  <div class="abs f-small" style="left:26px;top:967px">hello@oakharbor.example<br>Location:<br>4215 Mill Avenue, Tempe</div>
  <div class="abs f-head" style="left:142px;top:947px">Quick Links</div>
  <div class="abs f-list" style="left:142px;top:956px"><span class="on">Home</span><br>About<br>Service<br>Testimonials<br>Project<br>Contact</div>
  <div class="abs f-head" style="left:198px;top:947px">Resource</div>
  <div class="abs f-list" style="left:198px;top:956px"><span class="on">Help</span><br>About<br>Privacy Policy<br>Terms and Condition</div>
  <div class="abs f-head" style="left:258px;top:947px">2022 Oak Harbor</div>
  <div class="abs f-small" style="left:258px;top:956px">All Right Reserved.</div>
  <div class="abs socials"><i></i><i></i><i></i><i></i></div>
</main>
</body>
</html>
```